Clark County Assessor Canditate

We need a billboard ad for a political candidate Tessa Harrow who is running for Clark County Assessor in an upcoming election. Needs to be simple and to the point to get the people to see the name "Tessa Harrow" and what to vote for "Clark County Assessor" in Las Vegas, NV. Also the billboard visibility is best in the top side of the sign, so the information should be most prominent in the top right, middle, left sides.The size of the billboard is 14 ft Height X 48 ft Wide Also needs some bright colors that are noticable from a freeway viewed billboard.Designers - I need to have "Paid for by Tessa Harrow for Clark County Assessor" on the sign
I have uploaded a few headshots you can work with to create a design. Thank you,

http://tessaharrow-vote.info/

Voters

Political

• Name, what I am voting for, and some image that represents Las Vegas and/or Nevada

```html
<!DOCTYPE html>
<html lang="en">
<head>
<meta charset="utf-8">
<title>Tessa Harrow for Clark County Assessor – Billboard</title>
<link rel="stylesheet" href="https://fonts.googleapis.com/css2?family=Bebas+Neue&family=Montserrat:wght@700;800;900&display=swap">
<style>
  :root {
    --page-bg: #e9ebee;
    --board-dark: #1d1d1f;
    --board-white: #ffffff;
    --campaign-red: #ee0a0a;
    --ink-dark: #222224;
    --photo-dark: #262628;
    --photo-mid: #3a3a3d;
  }
  * { margin: 0; padding: 0; box-sizing: border-box; }
  html, body {
    width: 1200px;
    height: 583px;
    overflow: hidden;
    background: var(--page-bg);
  }
  .billboard {
    position: absolute;
    left: 40px;
    top: 128px;
    width: 1120px;
    height: 327px;
    background: var(--board-dark);
    overflow: hidden;
  }
  .billboard__bands {
    position: absolute;
    inset: 0;
    width: 1120px;
    height: 327px;
  }
  .billboard__band--red { fill: var(--campaign-red); }
  .billboard__band--white { fill: var(--board-white); }
  .candidate-photo {
    position: absolute;
    left: 800px;
    top: 0;
    width: 320px;
    height: 327px;
    background: radial-gradient(ellipse at 55% 45%, var(--photo-mid) 0%, var(--photo-dark) 70%);
  }
  .candidate-name {
    position: absolute;
    left: 0;
    width: 716px;
    top: 8px;
    text-align: center;
    font-family: "Montserrat", sans-serif;
    font-weight: 800;
    font-size: 76px;
    letter-spacing: -1.5px;
    line-height: 1;
    color: var(--ink-dark);
  }
  .vote-for {
    position: absolute;
    left: 0;
    width: 716px;
    top: 110px;
    text-align: center;
    font-family: "Montserrat", sans-serif;
    font-weight: 800;
    font-size: 40px;
    line-height: 1;
    color: var(--campaign-red);
  }
  .office-title {
    position: absolute;
    left: 33px;
    top: 176px;
    font-family: "Bebas Neue", sans-serif;
    font-size: 82px;
    line-height: 1;
    letter-spacing: 1px;
    color: var(--board-white);
    white-space: nowrap;
  }
  .paid-for {
    position: absolute;
    left: 35px;
    top: 284px;
    font-family: "Montserrat", sans-serif;
    font-weight: 700;
    font-size: 19px;
    line-height: 1;
    color: var(--board-white);
    white-space: nowrap;
  }
  .paid-for__accent { color: var(--campaign-red); }
</style>
</head>
<body>
  <main class="billboard">
    <svg class="billboard__bands" viewBox="0 0 1120 327" aria-hidden="true">
      <polygon class="billboard__band--red" points="0,0 806,0 720,263 0,263"/>
      <polygon class="billboard__band--white" points="0,0 768,0 716,161 0,161"/>
    </svg>

    <div class="candidate-photo" role="img" aria-label="Headshot of candidate Tessa Harrow smiling against a dark studio backdrop"></div>

    <h1 class="candidate-name">Tessa Harrow</h1>
    <p class="vote-for">VOTE FOR</p>
    <h2 class="office-title">CLARK COUNTY ASSESSOR</h2>
    <p class="paid-for"><span class="paid-for__accent">Paid for by</span> Tessa Harrow <span class="paid-for__accent">for</span> Clark County Assessor</p>
  </main>
</body>
</html>
```